Ridgeline Elite

Letter Head, Envelope, Business Cards, Social Media Banner (FB/Twitter), Social Media Icon, Social Media Announcement Template...

We are a Softball Team/Organization

Target Market(s)

High School Student-Athletes (softball players) and their parents

Font styles to use
Serif

Requirements
Must have
• Logo & Colors
Must POP and say WOW
Common theme amongst all designs

```html
<!DOCTYPE html>
<html lang="en">
<head>
<meta charset="utf-8">
<title>Ridgeline Elite — Business Card</title>
<link href="https://fonts.googleapis.com/css2?family=Montserrat:wght@400;500;600&family=Oswald:wght@600&display=swap" rel="stylesheet">
<style>
  :root {
    --navy: #14285e;
    --navy-deep: #0b1a45;
    --navy-light: #1c3472;
    --paper: #ffffff;
    --ink: #2b2f3a;
    --muted: #a9b1c6;
    --silver: #d7dbe4;
    --backdrop: #5e5e5e;
  }
  * { margin: 0; padding: 0; box-sizing: border-box; }
  html, body {
    width: 1200px; height: 800px; overflow: hidden;
    background: var(--backdrop);
  }
  .canvas {
    width: 1200px; height: 800px;
    display: flex; align-items: center; justify-content: center; gap: 40px;
  }
  .card {
    width: 540px; height: 309px; position: relative; overflow: hidden;
    box-shadow: 0 14px 30px rgba(0,0,0,0.35);
  }
  /* Front */
  .card-front { background: var(--paper); }
  .identity {
    position: absolute; left: 0; right: 0; top: 58px;
    display: flex; align-items: center; justify-content: center; gap: 22px;
  }
  .person { text-align: right; }
  .person-name {
    font-family: "Oswald", sans-serif; font-weight: 600;
    font-size: 27px; letter-spacing: 0.5px; color: var(--navy);
    line-height: 1.1; text-transform: uppercase;
  }
  .person-title {
    font-family: "Montserrat", sans-serif; font-size: 15px;
    color: var(--muted); letter-spacing: 1px;
  }
  .divider { width: 1px; height: 92px; background: #8a8f9c; }
  .contacts { list-style: none; font-family: "Montserrat", sans-serif; font-size: 13px; color: var(--ink); }
  .contacts li { display: flex; align-items: center; gap: 8px; line-height: 21px; }
  .contacts svg { width: 12px; height: 12px; flex: none; }
  .address-band {
    position: absolute; left: 0; right: 0; top: 222px; height: 36px;
    background: var(--navy);
    display: flex; align-items: center; justify-content: center;
    font-family: "Montserrat", sans-serif; font-weight: 500; font-size: 13.5px;
    color: var(--paper); letter-spacing: 0.3px;
  }
  /* Back */
  .card-back {
    background: radial-gradient(ellipse at 40% 55%, var(--navy-light), var(--navy) 55%, var(--navy-deep));
    display: flex; align-items: center; justify-content: center; gap: 14px;
  }
  .brand-dot { width: 16px; height: 16px; border-radius: 50%; background: var(--silver); }
  .brand-name {
    font-family: "Montserrat", sans-serif; font-weight: 600;
    font-size: 34px; letter-spacing: 3px; color: var(--silver);
    text-transform: uppercase;
  }
</style>
</head>
<body>
<main class="canvas">
  <section class="card card-front">
    <div class="identity">
      <div class="person">
        <p class="person-name">Daniel Hayes</p>
        <p class="person-title">President</p>
      </div>
      <div class="divider"></div>
      <ul class="contacts">
        <li>
          <svg viewBox="0 0 12 12"><path d="M3 1 L5 3.5 L4 5 Q5 7 7 8 L8.5 7 L11 9 L9.5 11 Q4 10.5 1 2.5 Z" fill="var(--navy)"/></svg>
          555-210-4417
        </li>
        <li>
          <svg viewBox="0 0 12 12"><rect x="3" y="1" width="6" height="10" rx="1" fill="none" stroke="var(--navy)" stroke-width="1.3"/></svg>
          555-318-2096
        </li>
        <li>
          <svg viewBox="0 0 12 12"><rect x="1" y="2.5" width="10" height="7" fill="var(--navy)"/><path d="M1 2.5 L6 6.5 L11 2.5" fill="none" stroke="#fff" stroke-width="1"/></svg>
          info@ridgelineelite.com
        </li>
        <li>
          <svg viewBox="0 0 12 12"><circle cx="6" cy="6" r="5" fill="var(--navy)"/><path d="M1 6 H11 M6 1 Q3 6 6 11 M6 1 Q9 6 6 11" fill="none" stroke="#fff" stroke-width="0.8"/></svg>
          www.ridgelineelite.com
        </li>
      </ul>
    </div>
    <div class="address-band">2816 Aspen Ridge Drive, Fairbanks, Alaska 99709</div>
  </section>

  <section class="card card-back">
    <span class="brand-dot"></span>
    <p class="brand-name">Ridgeline Elite</p>
  </section>
</main>
</body>
</html>
```